Tidewell Recovery Business Card Design

Professional and clean design. The design colors should flow with the logo. Two-sided card with the website on the back which is:

www.TidewellRecovery.example.

"Specializing in Water Damage Restoration"

On the front I need the name, email, phone, and logo.

Name: Dorian Vashti
Email: Dorian@TidewellRecovery.example
Phone: 555-318-2046 for now

I only have the Preview and Thumbnail right now but should have the source files uploaded within a day or two.

Target Market(s)

Flood victims, home owners with water damage from busted pipes etc...

Industry/Entity Type

Business

Contact Information for Business Card

Name: Dorian Vashti

Font styles to use
Serif
Sans Serif

```html
<!DOCTYPE html>
<html lang="en">
<head>
<meta charset="utf-8">
<title>Tidewell Recovery Business Card</title>
<link rel="stylesheet" href="https://fonts.googleapis.com/css2?family=Arimo:wght@400&family=Cinzel:wght@500&display=swap">
<style>
  :root {
    --page: #ffffff;
    --silver: #d9dadb;
    --silver-light: #e4e5e6;
    --frame-teal: #5fcbd3;
    --ocean: #479ed3;
    --wave-teal: #66ccd4;
    --wave-slate: #6d9caa;
    --wave-mist: #8fc3d6;
    --brand-blue: #4a93c9;
    --ink: #111111;
    --back-text: #d7e9f5;
    --back-mark: rgba(255, 255, 255, 0.16);
  }
  html, body {
    margin: 0;
    padding: 0;
    width: 1200px;
    height: 368px;
    overflow: hidden;
    background: var(--page);
  }
  .card {
    position: absolute;
    top: 0;
    height: 368px;
    overflow: hidden;
  }
  .card-front {
    left: 0;
    width: 578px;
    background:
      repeating-linear-gradient(0deg, rgba(255,255,255,0.18) 0 1px, transparent 1px 3px),
      repeating-linear-gradient(90deg, rgba(0,0,0,0.03) 0 1px, transparent 1px 4px),
      linear-gradient(180deg, var(--silver-light), var(--silver));
  }
  .front-art {
    position: absolute;
    inset: 0;
  }
  .brand-mark {
    position: absolute;
    left: 254px;
    top: 10px;
    width: 72px;
    height: 72px;
    border-radius: 50%;
    background: var(--brand-blue);
  }
  .brand-name {
    position: absolute;
    left: 0;
    width: 578px;
    top: 112px;
    margin: 0;
    text-align: center;
    font-family: "Cinzel", serif;
    font-weight: 500;
    font-size: 38px;
    line-height: 1.05;
    letter-spacing: 1px;
    color: var(--brand-blue);
  }
  .contact {
    position: absolute;
    left: 0;
    width: 578px;
    text-align: center;
    font-family: "Arimo", sans-serif;
    font-size: 16px;
    margin: 0;
  }
  .contact-line { top: 198px; }
  .contact-name { color: var(--brand-blue); }
  .contact-email { color: var(--ink); }
  .contact-phone { top: 226px; color: var(--brand-blue); padding-left: 2px; }
  .card-back {
    left: 622px;
    width: 578px;
    background: var(--ocean);
  }
  .tagline, .website {
    position: absolute;
    left: 0;
    width: 578px;
    margin: 0;
    text-align: center;
    font-family: "Arimo", sans-serif;
    color: var(--back-text);
  }
  .tagline { top: 40px; font-size: 22px; }
  .website { top: 312px; font-size: 21px; }
  .back-mark {
    position: absolute;
    left: 186px;
    top: 82px;
    width: 210px;
    height: 210px;
    border-radius: 50%;
    background: var(--back-mark);
  }
</style>
</head>
<body>
  <section class="card card-front">
    <svg class="front-art" width="578" height="368" viewBox="0 0 578 368" aria-hidden="true">
      <rect x="0" y="25" width="578" height="6" fill="var(--frame-teal)"/>
      <rect x="34" y="31" width="5" height="222" fill="var(--frame-teal)"/>
      <rect x="535" y="31" width="6" height="196" fill="var(--frame-teal)"/>
      <path d="M0 252 C90 262 170 280 260 270 C360 258 450 228 578 226 L578 368 L0 368 Z" fill="var(--wave-slate)"/>
      <path d="M0 262 C100 270 180 292 270 282 C370 270 460 246 578 240 L578 368 L0 368 Z" fill="var(--wave-teal)"/>
      <path d="M0 270 C110 280 200 302 290 294 C380 286 470 266 578 262 L578 368 L0 368 Z" fill="var(--wave-mist)"/>
      <path d="M0 282 C110 290 210 316 300 312 C390 308 480 286 578 282 L578 368 L0 368 Z" fill="var(--ocean)"/>
    </svg>
    <div class="brand-mark"></div>
    <h1 class="brand-name">Tidewell Recovery</h1>
    <p class="contact contact-line"><span class="contact-name">Dorian Vashti - </span> <span class="contact-email">Dorian@TidewellRecovery.example</span></p>
    <p class="contact contact-phone">Ph: 555-318-2046</p>
  </section>

  <section class="card card-back">
    <p class="tagline">"Specializing in Water Damage Restoration"</p>
    <div class="back-mark"></div>
    <p class="website">www.TidewellRecovery.example.</p>
  </section>
</body>
</html>
```